Business Card Design

I need a business card design for my law office based in Pasadena, California. I am a sole practitioner and I specialize in business transaction and litigation, probate and estate planning, taxation law, corporate and business formation, immigration and real estate. I want something that is simple, yet stands out.

A friend helped to create a logo about 6 years ago. I am open to new ideas to changing the logo.

Industry/Entity Type

Business

Contact Information for Business Card

Law Offices of Dorvan L. Mabry
842 W. Larkspur Ave., Suite 319
Pasadena, CA 90287
Tel: 626-555-0174
Fax: 626-555-0139
Email: dmabry@dlmlegalgroup.example

Attorney: Dorvan L. Mabry

```html
<!DOCTYPE html>
<html lang="en">
<head>
<meta charset="utf-8">
<title>Mabry Law Office — Business Card</title>
<link rel="stylesheet" href="https://fonts.googleapis.com/css2?family=Open+Sans:wght@400;600&display=swap">
<style>
  :root {
    --backdrop: #e6e6e6;
    --paper: #fbfbfb;
    --ink: #333333;
    --ink-soft: #555555;
    --rule: #666666;
    --band-light: #9a9a9a;
    --band-dark: #4c4c4c;
  }
  * { margin: 0; padding: 0; box-sizing: border-box; }
  html, body {
    width: 1200px; height: 720px; overflow: hidden;
    background: var(--backdrop);
    font-family: "Open Sans", sans-serif;
    color: var(--ink);
  }
  .canvas { position: relative; width: 1200px; height: 720px; }
  .card {
    position: absolute; top: 240px;
    width: 420px; height: 240px;
    background: var(--paper);
    overflow: hidden;
  }
  .card--front { left: 147px; }
  .card--back { left: 633px; }

  .tone-band { position: absolute; top: 0; bottom: 0; width: 70px; }
  .card--front .tone-band {
    right: 0;
    background: linear-gradient(90deg, var(--band-light), var(--band-dark));
  }
  .card--back .tone-band {
    left: 0;
    background: linear-gradient(90deg, var(--band-dark), var(--band-light));
  }

  .brand { position: absolute; left: 18px; top: 54px; display: flex; align-items: center; gap: 7px; }
  .brand__square { width: 48px; height: 48px; background: var(--ink); }
  .brand__name {
    font-size: 9.5px; font-weight: 600; letter-spacing: 0.6px;
    text-transform: uppercase; color: var(--ink); white-space: nowrap;
  }

  .contact { position: absolute; left: 180px; top: 86px; width: 162px; }
  .contact__head { display: flex; align-items: baseline; justify-content: space-between; }
  .contact__name { font-size: 14px; font-weight: 600; color: var(--ink); white-space: nowrap; }
  .contact__role { font-size: 9.5px; color: var(--ink-soft); }
  .contact__rule { height: 1px; background: var(--rule); margin: 4px 0 6px; }
  .contact__line { font-size: 10px; line-height: 15px; color: var(--ink-soft); white-space: nowrap; }

  .wordmark {
    position: absolute; left: 146px; top: 104px; width: 240px;
    text-align: center; white-space: nowrap;
    font-size: 16px; font-weight: 600; letter-spacing: 2px;
    text-transform: uppercase; color: var(--ink);
  }
</style>
</head>
<body>
<main class="canvas">
  <section class="card card--front" aria-label="Card front">
    <div class="tone-band" role="img" aria-label="Decorative grey panel area"></div>

    <div class="brand">
      <span class="brand__square"></span>
      <span class="brand__name">Mabry Law Office</span>
    </div>

    <div class="contact">
      <div class="contact__head">
        <span class="contact__name">Dorvan L. Mabry</span>
        <span class="contact__role">Attorney</span>
      </div>
      <div class="contact__rule"></div>
      <p class="contact__line">626-555-0174</p>
      <p class="contact__line">626-555-0139</p>
      <p class="contact__line">dmabry@dlmlegalgroup.example</p>
      <div class="contact__rule"></div>
      <p class="contact__line">842 W. Larkspur Ave., Suite 319</p>
      <p class="contact__line">Pasadena, CA 90287</p>
    </div>
  </section>

  <section class="card card--back" aria-label="Card back">
    <div class="tone-band" role="img" aria-label="Decorative grey panel area"></div>
    <p class="wordmark">Mabry Law Office</p>
  </section>
</main>
</body>
</html>
```